Tri-fold flyer Accumulator Clamp

Based on the information on our website http://www.trelvo-fixings.com
we require a A4 flyer for our Accumulator Clamp product. The flyer should be folded in 3 equal parts from landscape position. Colors of brochure based on website, product details can be copied from website and product specifications can be copied from our website.

Target Market(s)

OEM manufactures in US

Industry/Entity Type

Manufacturer

Font styles to use
Sans Serif

Colors

Designer to choose colors to be used in the design.

Requirements
Must have
• Product specifications as mentioned on website, including grid with details.
• Colors based on website.
Nice to have
• Application of this product as mentioned on website

```html
<!DOCTYPE html>
<html lang="en">
<head>
<meta charset="utf-8">
<title>Accumulator Clamps – Tri-fold Flyer</title>
<link href="https://fonts.googleapis.com/css2?family=Lato:wght@400;700;900&family=Oswald:wght@500;600&display=swap" rel="stylesheet">
<style>
:root{
  --navy:#1e3a4c;
  --teal:#1ba58c;
  --gold:#e8a321;
  --green:#3cb56a;
  --white:#ffffff;
  --mist:#cfdde4;
  --page:#e9ecee;
}
*{box-sizing:border-box;margin:0;padding:0}
html,body{width:1200px;height:1200px;overflow:hidden;background:var(--page);font-family:'Lato',sans-serif;color:var(--white)}
.spread{position:absolute;left:198px;width:804px;height:568px;display:flex;box-shadow:0 6px 18px rgba(0,0,0,.18)}
.spread--outside{top:22px}
.spread--inside{top:610px}
.panel{position:relative;width:268px;height:568px;overflow:hidden}
.rotated{position:absolute;left:0;top:0;width:568px;height:268px;transform-origin:0 0;transform:translateY(568px) rotate(-90deg)}

/* specs panel */
.specs{background:var(--navy);padding:46px 26px 0 26px}
.spec{display:flex;gap:12px;margin-bottom:24px}
.spec svg{flex:0 0 24px;width:24px;height:24px;margin-top:10px}
.spec h3{font-size:12px;font-weight:900;letter-spacing:.5px;text-transform:uppercase;margin-bottom:3px}
.spec p{font-size:9.5px;line-height:1.4;color:var(--mist)}

/* back panel */
.back{background:var(--teal)}
.back-shapes{position:absolute;inset:0;width:268px;height:568px}
.contact{position:absolute;top:196px;left:0;width:100%;text-align:center}
.brand{display:inline-flex;align-items:center;gap:8px;font-weight:900;font-size:20px;letter-spacing:1px;color:var(--white)}
.brand i{display:block;width:16px;height:16px;border-radius:50%;background:var(--white)}
.contact ul{list-style:none;margin-top:16px}
.contact li{font-size:9.5px;margin-bottom:8px;display:flex;flex-direction:column;align-items:center;gap:3px}
.contact li svg{width:14px;height:14px}
.contact .url{font-size:9px;letter-spacing:1px;margin-top:4px;border-top:1px solid rgba(255,255,255,.5);padding-top:6px;display:inline-block}

/* cover */
.cover{background:var(--navy)}
.cover .brand{position:absolute;top:34px;left:0;width:100%;justify-content:center;font-size:20px}
.product{position:absolute;top:90px;left:34px;width:200px;height:200px;border-radius:50%;background:radial-gradient(circle,#ffffff 40%,#d9dee1 100%)}
.product-ring{position:absolute;top:84px;left:28px;width:212px;height:212px}
.cover h1{position:absolute;top:322px;left:0;width:100%;text-align:center;font-family:'Oswald',sans-serif;font-weight:600;font-size:25px;letter-spacing:.5px}
.cover p{position:absolute;top:370px;left:30px;right:30px;text-align:center;font-size:10px;line-height:1.5;color:var(--mist)}
.cover .url{position:absolute;bottom:40px;left:40px;right:40px;text-align:center;font-size:9px;letter-spacing:1px;border-top:1px solid rgba(255,255,255,.4);padding-top:6px}

/* drawings */
.drawings{background:var(--navy)}
.drawing{position:absolute;top:50px;width:230px;height:180px;border-radius:4px;background:linear-gradient(135deg,rgba(255,255,255,.10),rgba(255,255,255,.03));border:1px solid rgba(255,255,255,.15)}
.drawing--type1{left:30px}
.drawing--type2{left:300px}
.drawing-label{position:absolute;top:14px;font-family:'Oswald',sans-serif;font-size:14px}
.drawing-label--type1{left:40px}
.drawing-label--type2{left:310px}

/* table */
.specs-table-panel{background:var(--teal)}
.grid{position:absolute;left:18px;top:24px;width:532px;border-collapse:collapse;font-size:9px;text-align:center}
.grid th{font-weight:700;font-size:8px;padding:6px 2px;color:var(--white)}
.grid td{padding:5px 2px;color:var(--navy)}
.grid tbody tr:nth-child(odd) td{background:var(--white)}
.grid tbody tr:nth-child(even) td{color:var(--white)}
.grid td:first-child{font-weight:700}

/* applications */
.applications{background:var(--navy)}
.apps-heading{position:absolute;left:18px;top:16px;display:flex;align-items:center;gap:10px;font-family:'Oswald',sans-serif;font-size:15px;letter-spacing:1px}
.apps-heading span{display:block;width:420px;height:1px;background:rgba(255,255,255,.5)}
.apps{position:absolute;left:18px;top:54px;display:flex;gap:10px}
.app{width:126px;height:196px;background:var(--white);color:var(--navy)}
.app-photo{height:110px}
.app-photo--gas{background:linear-gradient(180deg,#d8353b,#a91f26)}
.app-photo--fork{background:linear-gradient(180deg,#5a6b74,#1f2a30)}
.app-photo--wind{background:linear-gradient(180deg,#7eaed1,#e6cfd0)}
.app-photo--station{background:linear-gradient(180deg,#b98a52,#7c858b)}
.app h4{font-size:9px;font-weight:900;text-transform:uppercase;padding:6px 8px 2px}
.app p{font-size:8px;line-height:1.35;padding:0 8px 8px}
</style>
</head>
<body>

<section class="spread spread--outside">
  <div class="panel specs">
    <div class="spec">
      <svg viewBox="0 0 24 24" fill="none" stroke="#e8a321" stroke-width="2"><rect x="3" y="6" width="18" height="12"/><path d="M3 12h18"/></svg>
      <div><h3>Materials</h3><p>Cold rolled carbon steel (AISI-SAE 1010)<br>Cold rolled stainless steel (AISI-SAE 316)<br>Other materials upon your request</p></div>
    </div>
    <div class="spec">
      <svg viewBox="0 0 24 24" fill="none" stroke="#e8a321" stroke-width="2"><rect x="5" y="5" width="14" height="14"/><path d="M3 21L21 3"/></svg>
      <div><h3>Sizes</h3><p>Standard diameter range 3" to 10"<br>Other diameters and sizes upon your request</p></div>
    </div>
    <div class="spec">
      <svg viewBox="0 0 24 24" fill="#e8a321"><circle cx="7" cy="7" r="3"/><circle cx="17" cy="7" r="3"/><rect x="4" y="13" width="16" height="7" rx="2"/></svg>
      <div><h3>Assembly</h3><p>High quality, resistant spot welding (RSW)<br>Includes rubber cushioning and hardware</p></div>
    </div>
    <div class="spec">
      <svg viewBox="0 0 24 24" fill="none" stroke="#e8a321" stroke-width="2"><path d="M12 3l8 3v6c0 5-4 8-8 9-4-1-8-4-8-9V6z"/></svg>
      <div><h3>Finishes</h3><p>Zinc plated<br>Pickled and passivated<br>Other finishes upon your request</p></div>
    </div>
    <div class="spec">
      <svg viewBox="0 0 24 24" fill="none" stroke="#e8a321" stroke-width="2"><path d="M4 20L20 4M6 14l4 4M10 10l4 4"/></svg>
      <div><h3>Design</h3><p>Extremely safe: upper clamp half connects straight to the mounting bracket instead of the lower clamp half. This ensures that the accumulator is secure at all times.</p></div>
    </div>
    <div class="spec">
      <svg viewBox="0 0 24 24" fill="none" stroke="#e8a321" stroke-width="2.4"><path d="M3 7h5l8 10h5M3 17h5l8-10h5M18 4l3 3-3 3M18 14l3 3-3 3"/></svg>
      <div><h3>Types</h3><p>Single bolt type<br>Double bolt type<br>Other types upon your request<br>Rounded steel eliminates sharp edges</p></div>
    </div>
  </div>

  <div class="panel back">
    <svg class="back-shapes" viewBox="0 0 268 568">
      <defs>
        <linearGradient id="sky" x1="0" y1="0" x2="0" y2="1"><stop offset="0" stop-color="#6fa7cf"/><stop offset=".6" stop-color="#b9d4e6"/><stop offset="1" stop-color="#e9c8c4"/></linearGradient>
        <linearGradient id="parts" x1="0" y1="0" x2="1" y2="1"><stop offset="0" stop-color="#9aa3a8"/><stop offset=".5" stop-color="#5d666c"/><stop offset="1" stop-color="#c6ccd0"/></linearGradient>
      </defs>
      <polygon points="0,0 268,0 268,118 0,166" fill="url(#sky)" role="img" aria-label="Photo of wind turbines against a pale evening sky"/>
      <polygon points="0,166 268,118 268,124 0,172" fill="#e8a321"/>
      <polygon points="0,448 268,412 268,568 0,568" fill="url(#parts)" role="img" aria-label="Photo of a pile of stainless steel clamps"/>
      <polygon points="0,442 268,406 268,412 0,448" fill="#e8a321"/>
    </svg>
    <div class="contact">
      <div class="brand"><i></i>TRELVO FIXINGS</div>
      <ul>
        <li><svg viewBox="0 0 24 24" fill="#fff"><path d="M12 3l9 8h-3v9H6v-9H3z"/></svg>4820 Harlow Ave Suite 210, Brenton, TX 77512</li>
        <li><svg viewBox="0 0 24 24" fill="none" stroke="#fff" stroke-width="2"><rect x="3" y="6" width="18" height="12"/><path d="M3 6l9 7 9-7"/></svg>info@trelvo-fixings.com</li>
        <li><svg viewBox="0 0 24 24" fill="#fff"><path d="M6 3l4 4-2 3c1 2 4 5 6 6l3-2 4 4-3 3C10 21 3 14 3 6z"/></svg>1-713-555-0148</li>
      </ul>
      <span class="url">www.trelvo-fixings.com</span>
    </div>
  </div>

  <div class="panel cover">
    <div class="brand"><i></i>TRELVO FIXINGS</div>
    <div class="product" role="img" aria-label="Product photo of a steel accumulator clamp with rubber lining"></div>
    <svg class="product-ring" viewBox="0 0 212 212" fill="none" stroke-width="5">
      <path d="M106 3 A103 103 0 0 0 30 176" stroke="#e8a321"/>
      <path d="M30 176 A103 103 0 0 0 209 106" stroke="#e8a321"/>
      <path d="M209 106 A103 103 0 0 0 106 3" stroke="#3cb56a"/>
    </svg>
    <h1>ACCUMULATOR CLAMPS</h1>
    <p>Accumulator clamps are used to safely mount hydraulic accumulators. Trelvo Fixings, Inc. has over 35 years of experience in designing and manufacturing mounting clamps and brackets for hydraulic accumulators.</p>
    <div class="url">www.trelvo-fixings.com</div>
  </div>
</section>

<section class="spread spread--inside">
  <div class="panel drawings">
    <div class="rotated">
      <span class="drawing-label drawing-label--type1">Type 1</span>
      <span class="drawing-label drawing-label--type2">Type 2</span>
      <div class="drawing drawing--type1" role="img" aria-label="Technical drawing of the Type 1 clamp with dimensions"></div>
      <div class="drawing drawing--type2" role="img" aria-label="Technical drawing of the Type 2 clamp with dimensions"></div>
    </div>
  </div>

  <div class="panel specs-table-panel">
    <div class="rotated">
      <table class="grid">
        <thead><tr><th>Item Code</th><th>Type</th><th>Min Range</th><th>Max Range</th><th>Height</th><th>Width</th><th>Thickness</th><th>Band Width</th><th>Pitch</th><th>Hole Size</th><th>Bracket Type</th></tr></thead>
        <tbody>
          <tr><td>AS2-18792</td><td>2</td><td>8.7</td><td>9.2</td><td>9.2</td><td>5</td><td>1.6</td><td>1.2</td><td>9</td><td>0.7</td><td>ASB-1L</td></tr>
          <tr><td>AS1-16669</td><td>1</td><td>6.6</td><td>6.9</td><td>6.9</td><td>4</td><td>1.38</td><td>1.2</td><td>6.3</td><td>0.4</td><td>ASB-1M</td></tr>
          <tr><td>AS2-19196</td><td>2</td><td>9.1</td><td>9.6</td><td>9.6</td><td>5.1</td><td>1.6</td><td>1.2</td><td>9</td><td>0.7</td><td>ASB-1L</td></tr>
          <tr><td>AS2-199105</td><td>2</td><td>9.9</td><td>10.5</td><td>10.5</td><td>5.6</td><td>1.6</td><td>1.2</td><td>9</td><td>0.7</td><td>ASB-1L</td></tr>
          <tr><td>AS1-14447</td><td>1</td><td>4.4</td><td>4.7</td><td>4.7</td><td>3</td><td>1.38</td><td>1.2</td><td>3.9</td><td>0.4</td><td>ASB-1S</td></tr>
          <tr><td>AS1-14851</td><td>1</td><td>4.8</td><td>5.1</td><td>5.1</td><td>3</td><td>1.38</td><td>1.2</td><td>3.9</td><td>0.4</td><td>ASB-1S</td></tr>
          <tr><td>AS2-16671</td><td>2</td><td>6.6</td><td>7.1</td><td>7.1</td><td>4.1</td><td>1.57</td><td>1.2</td><td>6.3</td><td>0.4</td><td>ASB-1M</td></tr>
          <tr><td>AS2-17075</td><td>2</td><td>7</td><td>7.5</td><td>7.5</td><td>4.1</td><td>1.6</td><td>1.2</td><td>6.3</td><td>0.4</td><td>ASB-1M</td></tr>
        </tbody>
      </table>
    </div>
  </div>

  <div class="panel applications">
    <div class="rotated">
      <div class="apps-heading">APPLICATIONS<span></span></div>
      <div class="apps">
        <article class="app">
          <div class="app-photo app-photo--station" role="img" aria-label="Photo of rows of accumulator bottles in a station"></div>
          <h4>Accumulator Stations</h4>
          <p>Accumulator clamps are used in accumulator stations to securely mount the hydraulic accumulators.</p>
        </article>
        <article class="app">
          <div class="app-photo app-photo--wind" role="img" aria-label="Photo of a wind turbine at dusk"></div>
          <h4>Wind Turbines</h4>
          <p>Wind turbines often use hydraulic systems for pitch and braking. Our brackets hold these accumulators firmly.</p>
        </article>
        <article class="app">
          <div class="app-photo app-photo--fork" role="img" aria-label="Photo of a forklift hydraulic assembly"></div>
          <h4>Forklifts</h4>
          <p>Many forklifts use gas as a source of power. Our clamps mount these cylinders safely.</p>
        </article>
        <article class="app">
          <div class="app-photo app-photo--gas" role="img" aria-label="Photo of red gas cylinders mounted in a row"></div>
          <h4>Gas Cylinders</h4>
          <p>Our accumulator clamps are used to secure gas cylinders in fire systems.</p>
        </article>
      </div>
    </div>
  </div>
</section>

</body>
</html>
```